LBH Letterhead

I need letterhead for "lakeside birch holdings llc" ...

logo attached to project..

Company Info:
482 East Marlow Avenue, Suite 7B
Chicago, Illinois 60917
ofc 312-555-0148
facsimile 312-555-0193
www.lakesidebirchholdingsllc.example
info@lakesidebirchholdingsllc.example

I have multiple projects listed.. see below:

Business cards for lakeside birch holdings llc
letterhead "
envelopes "

Business cards for KV Commerce LLC
letterhead "
envelopes "

```html
<!DOCTYPE html>
<html lang="en">
<head>
<meta charset="utf-8">
<title>Lakeside Birch Holdings LLC Letterhead</title>
<link rel="stylesheet" href="https://fonts.googleapis.com/css2?family=Cinzel:wght@500&family=Fira+Sans:wght@400&display=swap">
<style>
  :root {
    --band-light: #2a7ff0;
    --band-mid: #1553d6;
    --band-dark: #0a2fa8;
    --ink-blue: #1c3fa8;
    --footer-blue: #1a2f9c;
    --rule-blue: #3b5bd0;
    --paper: #ffffff;
  }
  html, body {
    margin: 0;
    padding: 0;
    width: 848px;
    height: 1200px;
    overflow: hidden;
    background: var(--paper);
  }
  .letterhead {
    position: relative;
    width: 848px;
    height: 1200px;
    background: var(--paper);
    overflow: hidden;
  }
  .header-band {
    position: absolute;
    top: 0;
    left: 0;
    width: 848px;
    height: 116px;
    display: block;
  }
  .brand-name {
    position: absolute;
    top: 86px;
    left: 0;
    width: 848px;
    margin: 0;
    text-align: center;
    font-family: "Cinzel", serif;
    font-weight: 500;
    font-size: 13.5px;
    letter-spacing: 0.4px;
    color: var(--ink-blue);
    white-space: nowrap;
  }
  .brand-mark {
    position: absolute;
    top: 30px;
    left: 400px;
    width: 48px;
    height: 48px;
    border-radius: 50%;
    background: var(--ink-blue);
  }
  .contact-footer {
    position: absolute;
    bottom: 22px;
    left: 0;
    width: 848px;
    display: flex;
    justify-content: center;
    align-items: center;
    gap: 22px;
    font-family: "Fira Sans", sans-serif;
    font-size: 12.5px;
    line-height: 1.35;
    color: var(--footer-blue);
    text-align: center;
  }
  .contact-block { margin: 0; }
  .contact-divider {
    width: 1px;
    height: 20px;
    background: var(--rule-blue);
  }
</style>
</head>
<body>
  <div class="letterhead">
    <svg class="header-band" viewBox="0 0 848 116" xmlns="http://www.w3.org/2000/svg" aria-hidden="true">
      <defs>
        <linearGradient id="bandGradient" x1="0" y1="0" x2="1" y2="0.3">
          <stop offset="0" stop-color="var(--band-light)"/>
          <stop offset="0.45" stop-color="var(--band-mid)"/>
          <stop offset="1" stop-color="var(--band-dark)"/>
        </linearGradient>
      </defs>
      <rect width="848" height="116" fill="url(#bandGradient)"/>
      <polygon points="90,0 140,0 110,116 60,116" fill="#ffffff" opacity="0.06"/>
      <polygon points="640,0 700,0 680,116 620,116" fill="#ffffff" opacity="0.05"/>
      <polygon points="760,0 848,0 848,116 790,116" fill="#001a80" opacity="0.18"/>
      <circle cx="424" cy="52" r="128" fill="var(--paper)"/>
    </svg>
    <span class="brand-mark" aria-hidden="true"></span>
    <p class="brand-name">Lakeside Birch Holdings LLC</p>

    <footer class="contact-footer">
      <p class="contact-block">482 East Marlow Avenue, Suite 7B<br>Chicago, Illinois 60917</p>
      <span class="contact-divider"></span>
      <p class="contact-block">ofc 312-555-0148<br>facsimile 312-555-0193</p>
      <span class="contact-divider"></span>
      <p class="contact-block">www.lakesidebirchholdingsllc.example<br>info@lakesidebirchholdingsllc.example</p>
    </footer>
  </div>
</body>
</html>
```